Falcrest security business card

Looking for a business card for my security company

Target Market(s)

Security

Industry/Entity Type

Security

Contact Information for Business Card

Name - Gil Marston. Title - General manager - direct 314 862.4490 website www. falcrestsecurityservices.example email - gil@ falcrestsecurityservices.example

Requirements
Must have
• Logo attached

```html
<!DOCTYPE html>
<html lang="en">
<head>
<meta charset="utf-8">
<title>Falcrest Security Services – Business Card</title>
<link href="https://fonts.googleapis.com/css2?family=Lato:wght@400;700&display=swap" rel="stylesheet">
<style>
  :root {
    --page-bg: #9a9b9a;
    --card-bg: #1a1a1a;
    --gold: #d4a94e;
    --gold-soft: rgba(212, 169, 78, 0.10);
    --text-light: #f2f2f2;
  }
  * { margin: 0; padding: 0; box-sizing: border-box; }
  html, body {
    width: 1200px; height: 1200px; overflow: hidden;
    background: var(--page-bg);
    font-family: 'Lato', sans-serif;
  }
  .card {
    position: absolute; left: 222px; width: 755px; height: 463px;
    background: var(--card-bg); overflow: hidden;
  }
  .card--front { top: 105px; }
  .card--back { top: 630px; }

  .decor {
    position: absolute; border-radius: 50%;
    background: radial-gradient(circle, var(--gold-soft) 0%, transparent 70%);
  }
  .decor--front-top { right: 0; top: 0; width: 240px; height: 170px; }
  .decor--front-bottom { right: 110px; bottom: 0; width: 150px; height: 130px; }
  .decor--back-left { left: 0; top: 60px; width: 220px; height: 200px; }
  .decor--back-right { right: 0; top: 60px; width: 220px; height: 200px; }

  .brand {
    position: absolute; display: flex; align-items: center;
    color: var(--gold); font-weight: 700; letter-spacing: 1px;
  }
  .brand__mark { background: var(--gold); }
  .brand--small { left: 46px; top: 100px; font-size: 46px; gap: 12px; }
  .brand--small .brand__mark { width: 16px; height: 16px; }
  .brand--large {
    left: 0; right: 0; top: 175px; justify-content: center;
    font-size: 92px; gap: 22px;
  }
  .brand--large .brand__mark { width: 30px; height: 30px; }

  .person { position: absolute; right: 43px; top: 210px; text-align: right; }
  .person__name { color: var(--gold); font-size: 30px; font-weight: 400; line-height: 1.1; }
  .person__title { color: var(--text-light); font-size: 20px; font-weight: 400; margin-top: 4px; }

  .divider {
    position: absolute; left: 44px; right: 43px; top: 296px;
    height: 2px; background: var(--gold);
  }

  .contacts { position: absolute; left: 46px; top: 322px; list-style: none; }
  .contacts__item {
    display: flex; align-items: center; gap: 10px;
    color: var(--text-light); font-size: 20px; height: 32px;
  }
  .contacts__icon { width: 22px; height: 22px; flex: none; }
</style>
</head>
<body>

<section class="card card--front">
  <div class="decor decor--front-top" role="img" aria-label="Faint star decoration"></div>
  <div class="decor decor--front-bottom" role="img" aria-label="Faint star decoration"></div>

  <div class="brand brand--small"><span class="brand__mark"></span>Falcrest</div>

  <div class="person">
    <p class="person__name">Gil Marston</p>
    <p class="person__title">General manager</p>
  </div>

  <div class="divider"></div>

  <ul class="contacts">
    <li class="contacts__item">
      <svg class="contacts__icon" viewBox="0 0 24 24" fill="#d4a94e"><path d="M3 9c0-3 18-3 18 0v2h-4V9H7v2H3z"/><rect x="5" y="12" width="14" height="9" rx="2"/><circle cx="12" cy="16.5" r="2.5" fill="#1a1a1a"/></svg>
      314 862.4490
    </li>
    <li class="contacts__item">
      <svg class="contacts__icon" viewBox="0 0 24 24" fill="none" stroke="#d4a94e" stroke-width="2"><rect x="2" y="5" width="18" height="13"/><path d="M2 5l9 7 9-7"/></svg>
      gil@ falcrestsecurityservices.example
    </li>
    <li class="contacts__item">
      <svg class="contacts__icon" viewBox="0 0 24 24" fill="none" stroke="#d4a94e" stroke-width="1.6"><circle cx="12" cy="12" r="9"/><ellipse cx="12" cy="12" rx="4" ry="9"/><path d="M3 12h18M5 7h14M5 17h14"/></svg>
      www. falcrestsecurityservices.example
    </li>
  </ul>
</section>

<section class="card card--back">
  <div class="decor decor--back-left" role="img" aria-label="Faint star decoration"></div>
  <div class="decor decor--back-right" role="img" aria-label="Faint star decoration"></div>
  <div class="brand brand--large"><span class="brand__mark"></span>Falcrest</div>
</section>

</body>
</html>
```